Business Card design for construction company

I would like a business card design for a construction company - ORD Builders. I have attached the ai logo file for use. I would like the card to be very smart and clean and incorporate only white and the two colours in the logo. I would like the card to have two sides. One side can just have the logo, the other with the relevant information.

Target Market(s)

Building and Construction Clients

Industry/Entity Type

Business

Contact Information for Business Card

Name: Tom Harcliffe
Company: ORD Builders Pty Limited
Address: 14 Mulberry Crescent Oakvale Heights 2093
Phone: 0432 517 208
Email: tomh@ordbuilders.example.au

Font styles to use
Serif
Sans Serif

Requirements
Must have
• Details noted above
• Logo as provided
• Colours as in logo
• Square edges
• A font that compliments the logo
Should not have
• Any colour other than white and those in logo
• Rounded edges

```html
<!DOCTYPE html>
<html lang="en">
<head>
<meta charset="utf-8">
<title>ORD Builders – Business Card</title>
<link rel="stylesheet" href="https://fonts.googleapis.com/css2?family=Michroma&family=Roboto:wght@400;500&display=swap">
<style>
  :root {
    --brand-blue: #0a86cf;
    --brand-blue-deep: #0076be;
    --brand-charcoal: #3a3a3c;
    --card-white: #f4f4f4;
    --card-white-shade: #e6e6e6;
    --text-dark: #2e2e30;
    --stage: #bdbdbd;
  }
  * { box-sizing: border-box; margin: 0; padding: 0; }
  html, body { width: 1200px; height: 576px; overflow: hidden; }
  body {
    background: var(--stage);
    position: relative;
    font-family: "Roboto", Arial, sans-serif;
  }
  .card {
    position: absolute;
    overflow: hidden;
  }
  /* Front side */
  .card-front {
    left: 82px; top: 139px; width: 484px; height: 293px;
    background: linear-gradient(180deg, var(--brand-blue) 0%, var(--brand-blue-deep) 100%);
  }
  .front-wordmark {
    position: absolute; left: 0; right: 0; top: 124px;
    text-align: center;
    font-family: "Michroma", "Arial", sans-serif;
    font-size: 26px; letter-spacing: 2px;
    color: #ffffff;
  }
  .front-web {
    position: absolute; left: 0; right: 0; top: 262px;
    display: flex; justify-content: center; align-items: center; gap: 14px;
    color: #ffffff; font-size: 12.5px;
  }
  .front-web .rule {
    width: 68px; height: 2px;
    background: linear-gradient(90deg, rgba(255,255,255,0), #ffffff 50%, rgba(255,255,255,0));
  }
  /* Back side */
  .card-back {
    left: 602px; top: 138px; width: 482px; height: 291px;
    background: linear-gradient(180deg, var(--card-white) 0%, var(--card-white-shade) 100%);
  }
  .back-wordmark {
    position: absolute; left: 26px; top: 44px;
    font-family: "Michroma", "Arial", sans-serif;
    font-size: 26px; letter-spacing: 2px;
    color: var(--text-dark);
  }
  .holder-name {
    position: absolute; left: 25px; top: 116px;
    font-family: "Michroma", "Arial", sans-serif;
    font-size: 18px; font-weight: 700; letter-spacing: 0.5px;
    color: var(--brand-blue);
    -webkit-text-stroke: 0.6px var(--brand-blue);
  }
  .holder-role {
    position: absolute; left: 25px; top: 142px;
    font-size: 11.5px; color: var(--text-dark);
  }
  .contact-list {
    position: absolute; left: 27px; top: 168px;
    list-style: none;
  }
  .contact-list li {
    display: flex; align-items: center; gap: 7px;
    height: 17.5px;
    font-size: 13px; color: var(--text-dark);
  }
  .contact-list svg { width: 10px; height: 10px; fill: var(--text-dark); flex: none; }
  .base-band {
    position: absolute; left: 0; right: 0; top: 224px; bottom: 0;
    background: linear-gradient(180deg, var(--brand-charcoal) 0%, var(--brand-blue) 45%, var(--brand-blue-deep) 100%);
  }
  .address {
    position: absolute; right: 31px; top: 234px;
    text-align: right; color: #ffffff;
    font-size: 12.5px; line-height: 17.5px;
    font-style: normal;
  }
</style>
</head>
<body>
  <section class="card card-front" aria-label="Card front">
    <div class="front-wordmark">ORD Builders</div>
    <div class="front-web">
      <span class="rule"></span>
      <span>www.ordbuilders.example.au</span>
      <span class="rule"></span>
    </div>
  </section>

  <section class="card card-back" aria-label="Card back">
    <div class="base-band" role="img" aria-label="Decorative flowing wave band in charcoal and blue"></div>

    <div class="back-wordmark">ORD Builders</div>
    <h1 class="holder-name">TOM HARCLIFFE</h1>
    <p class="holder-role">Managing Director</p>

    <ul class="contact-list">
      <li>
        <svg viewBox="0 0 10 10" aria-hidden="true"><path d="M1 3.2 C1 1.6 2.6 1 5 1 C7.4 1 9 1.6 9 3.2 L7 3.6 L6.6 2.6 L3.4 2.6 L3 3.6 Z M2.4 4.4 L7.6 4.4 L9 9 L1 9 Z"/></svg>
        <span>0432 517 208</span>
      </li>
      <li>
        <svg viewBox="0 0 10 10" aria-hidden="true"><path d="M0.5 2 L9.5 2 L5 5.6 Z M0.5 3 L5 6.6 L9.5 3 L9.5 8.2 L0.5 8.2 Z"/></svg>
        <span>tomh@ordbuilders.example.au</span>
      </li>
      <li>
        <svg viewBox="0 0 10 10" aria-hidden="true"><circle cx="5" cy="5" r="4.2" fill="none" stroke="var(--text-dark)" stroke-width="1"/><ellipse cx="5" cy="5" rx="1.8" ry="4.2" fill="none" stroke="var(--text-dark)" stroke-width="0.8"/><path d="M0.8 5 H9.2" stroke="var(--text-dark)" stroke-width="0.8"/></svg>
        <span>www.ordbuilders.example.au</span>
      </li>
    </ul>

    <address class="address">
      14 Mulberry Crescent<br>
      Oakvale Heights 2093
    </address>
  </section>
</body>
</html>
```